Business card design for Velvet Harbor

We need business cards designed for our new marketing consulting company, Velvet Harbor. Our services include marketing strategy, go-to-market and launch planning, growth strategy, and execution. We serve medical technology and health technology companies, from startups to well-established growth companies.

The business cards should feel professional, credible, reliable and trustworthy, and should instill confidence. Also bold, creative, and modern.

The design must use the Velvet Harbor logo.

The primary brand color is this orange: #FF5501
A secondary color that you can use is this gray: #282B2D
I would prefer only to use the orange and gray. But if you feel you really need an additional accent color (please use it very sparingly, as little as possible), you can use this blue for small accent purposes: #009FED

Attached are the logo files. The main logo is the one with a little bit of orange on the left and the rest is gray.

The business card should include the following:

Velvet Harbor logo
First name and last name
Title
Email address
Phone number and type (in whatever order looks best for the design
Website (the website does not need to be in the same block as the personal info)

For example:

Nessa Pryle
Founder & Principal
nessa@velvetharbor.com
+1.628.309.4156 mobile (can use "." or spaces in between blocks of numbers)
velvetharbor.com (somewhere on the card, it does not need to be with the personal info; and note that there is no "www." at the beginning)

Note that there will be no address listed on the business card.

Target Market(s)

Executives (CEO, head of marketing, head of sales) at medical technology and health technology companies, mostly in their 40s and older, well-educated, often with advanced degrees. They are strategic thinkers, responsible for budgets, and familiar with P&L. Their comfort with and trust in using outside consultants varies.

Industry/Entity Type

Medical technology and health technology companies.

Contact Information for Business Card

See project description

Font styles to use
Sans Serif

Requirements
Must have
• Logo and see Business card details section above.

```html
<!DOCTYPE html>
<html lang="en">
<head>
<meta charset="utf-8">
<title>Velvet Harbor — Business Card</title>
<link rel="stylesheet" href="https://fonts.googleapis.com/css2?family=Montserrat:wght@400;500;700&display=swap">
<style>
  :root {
    --page: #d6d7d8;
    --card: #1c1d1f;
    --card-deep: #161718;
    --orange: #ff5501;
    --white: #ffffff;
    --rule: #f2f2f2;
    --pattern-a: #202123;
    --pattern-b: #2c2e30;
  }
  * { box-sizing: border-box; margin: 0; padding: 0; }
  html, body {
    width: 1200px; height: 1108px; overflow: hidden;
    background: var(--page);
    font-family: "Montserrat", Arial, sans-serif;
  }
  .sheet {
    position: relative; width: 1200px; height: 1108px;
    display: flex; justify-content: center; align-items: center; gap: 60px;
  }
  .card {
    position: relative; width: 420px; height: 680px;
    background: var(--card); border-radius: 26px; overflow: hidden;
    color: var(--white);
    box-shadow: 0 18px 40px rgba(0,0,0,.28);
  }

  /* Front */
  .card--front { display: flex; flex-direction: column; align-items: center; }
  .brand { margin-top: 150px; display: flex; flex-direction: column; align-items: center; }
  .brand__dot {
    width: 18px; height: 18px; border-radius: 50%;
    background: var(--orange); margin-bottom: 26px;
  }
  .brand__name {
    font-weight: 700; font-size: 42px; line-height: 1.02;
    letter-spacing: .2em; text-transform: uppercase; text-align: center;
    padding-left: .2em; color: var(--white);
  }
  .person { margin-top: 52px; text-align: center; }
  .person__name { color: var(--orange); font-weight: 700; font-size: 30px; }
  .person__title { font-weight: 400; font-size: 20px; margin-top: 4px; letter-spacing: .02em; }
  .icon-row {
    width: 330px; margin-top: 20px;
    display: flex; align-items: center; gap: 10px;
  }
  .icon-row__rule { flex: 1; height: 1.5px; background: var(--rule); }
  .icon {
    width: 34px; height: 34px; border-radius: 4px; background: var(--orange);
    display: flex; align-items: center; justify-content: center;
  }
  .icon svg { width: 22px; height: 22px; }
  .contacts {
    margin-top: 16px; text-align: center;
    font-size: 20px; line-height: 1.38; font-weight: 400; font-style: normal;
  }
  .contacts__type { color: var(--orange); font-weight: 500; margin-left: 4px; }

  /* Back */
  .card__pattern {
    position: absolute; inset: 0;
    background: radial-gradient(circle at 80% 20%, var(--pattern-b), var(--pattern-a) 55%, var(--card-deep));
  }
  .back-brand {
    position: absolute; right: 40px; bottom: 150px;
    display: flex; align-items: center; gap: 18px;
  }
  .back-brand__dot { width: 14px; height: 14px; border-radius: 50%; background: var(--orange); }
  .back-brand__name {
    font-weight: 700; font-size: 26px; line-height: 1.05;
    letter-spacing: .2em; text-transform: uppercase; color: var(--white);
  }
</style>
</head>
<body>
<main class="sheet">

  <section class="card card--front" aria-label="Card front">
    <div class="brand">
      <span class="brand__dot"></span>
      <p class="brand__name">Velvet<br>Harbor</p>
    </div>

    <div class="person">
      <h1 class="person__name">Nessa Pryle</h1>
      <p class="person__title">Founder &amp; Principal</p>
    </div>

    <div class="icon-row">
      <span class="icon-row__rule"></span>
      <span class="icon" aria-label="Phone">
        <svg viewBox="0 0 24 24" fill="none" stroke="#1c1d1f" stroke-width="2" stroke-linejoin="round">
          <path d="M6 3h3l2 5-2 1.5a11 11 0 0 0 5.5 5.5L16 13l5 2v3a2 2 0 0 1-2 2A16 16 0 0 1 4 5a2 2 0 0 1 2-2z"/>
        </svg>
      </span>
      <span class="icon" aria-label="Email">
        <svg viewBox="0 0 24 24" fill="none" stroke="#1c1d1f" stroke-width="2" stroke-linejoin="round">
          <rect x="3" y="6" width="18" height="12" rx="1"/><path d="M3 6l9 7 9-7"/>
        </svg>
      </span>
      <span class="icon" aria-label="Website">
        <svg viewBox="0 0 24 24" fill="none" stroke="#1c1d1f" stroke-width="1.8">
          <circle cx="12" cy="12" r="9"/><ellipse cx="12" cy="12" rx="4" ry="9"/><path d="M3 12h18M5 7h14M5 17h14"/>
        </svg>
      </span>
      <span class="icon-row__rule"></span>
    </div>

    <address class="contacts">
      <p>+1.628.309.4156<span class="contacts__type">mobile</span></p>
      <p>nessa@velvetharbor.com</p>
      <p>velvetharbor.com</p>
    </address>
  </section>

  <section class="card card--back" aria-label="Card back">
    <div class="card__pattern" role="img" aria-label="Embossed pattern of repeating ring shapes across the dark card"></div>
    <div class="back-brand">
      <span class="back-brand__dot"></span>
      <p class="back-brand__name">Velvet<br>Harbor</p>
    </div>
  </section>

</main>
</body>
</html>
```